Document Processing Services and Solutions for School Systems

I am looking to design a brochure for both Digital and Paper use. I can supply the written content. Would be looking for an overall design of the brochure with provided content worked into it.

```html
<!DOCTYPE html>
<html lang="en">
<head>
<meta charset="utf-8">
<title>Keystone Records Inc — School Document Solutions</title>
<link href="https://fonts.googleapis.com/css2?family=Bebas+Neue&family=Carlito:wght@400;700&display=swap" rel="stylesheet">
<style>
:root{
  --blue:#2e3192;
  --blue-deep:#25287f;
  --gold:#c9980a;
  --ink:#1c1c1c;
  --paper:#ffffff;
  --stage:#e4e4e6;
}
*{box-sizing:border-box;margin:0;padding:0}
html,body{width:1200px;height:1200px;overflow:hidden;background:var(--stage)}
.display{font-family:"Bebas Neue",Impact,sans-serif;font-weight:400;letter-spacing:.2px}
.body-text{font-family:Carlito,Calibri,Arial,sans-serif}

.sheet{
  position:absolute;left:166px;top:30px;width:1147px;height:1506px;
  transform:scale(.757);transform-origin:0 0;background:var(--paper);
  box-shadow:0 10px 40px rgba(0,0,0,.25);
}
.hero{position:absolute;left:0;top:0;width:1147px;height:578px;overflow:hidden;
  background:linear-gradient(100deg,var(--blue-deep) 0%,var(--blue) 40%,#3a3fb0 60%,var(--blue) 100%)}
.hero-photo{position:absolute;left:200px;top:20px;width:760px;height:558px;
  background:radial-gradient(ellipse at 55% 40%,rgba(120,130,230,.35),rgba(46,49,146,0) 70%)}
.brand{position:absolute;left:0;top:56px;width:338px;height:118px;background:var(--paper);
  display:flex;align-items:center;justify-content:center;gap:12px}
.brand-mark{width:18px;height:18px;background:var(--gold)}
.brand-name{font-family:"Bebas Neue",Impact,sans-serif;font-size:40px;color:var(--blue);line-height:1;white-space:nowrap}
.headline{position:absolute;left:48px;top:236px;font-size:82px;line-height:97px;color:#fff;white-space:nowrap}
.gold{color:var(--gold)}

.intro-title{position:absolute;left:51px;top:600px;font-size:52px;line-height:56px;color:var(--blue);white-space:nowrap}
.intro{position:absolute;left:51px;top:662px;width:880px;font-size:19.5px;line-height:25px;color:var(--ink)}

.band{position:absolute;height:52px;padding-left:14px;font-size:38px;line-height:54px;color:#fff;white-space:nowrap;
  background:linear-gradient(90deg,var(--gold) 0%,#d9b84f 50%,rgba(243,231,192,0) 100%)}
.band-services{left:52px;top:763px;width:410px}
.band-why{left:45px;top:1120px;width:410px;height:50px;line-height:52px}

.service{position:absolute;top:828px}
.service-icon{position:absolute;left:0;top:0;width:74px;height:74px}
.service-title{position:absolute;top:10px;font-size:22px;line-height:24px;color:var(--blue);white-space:nowrap}
.service-list{position:absolute;top:80px;list-style:none;font-size:14px;line-height:17.5px;color:var(--ink)}
.service-list li{position:relative;padding-left:16px;margin-bottom:17px}
.service-list li::before{content:"";position:absolute;left:0;top:6px;width:4px;height:4px;background:var(--gold)}
.divider{position:absolute;top:862px;width:2px;height:211px;background:var(--gold)}

.reasons{position:absolute;left:55px;top:1190px;list-style:none}
.reason{position:relative;padding-left:33px;height:53px}
.reason svg{position:absolute;left:0;top:2px}
.reason-title{font-size:19px;line-height:20px;color:var(--gold);white-space:nowrap}
.reason-text{font-size:14px;line-height:18px;color:var(--ink);white-space:nowrap}

.cta{position:absolute;left:580px;top:1128px;width:496px;height:251px}
.cta-head{height:75px;padding:20px 0 0 31px;font-size:36px;line-height:44px;color:#fff;white-space:nowrap;
  background:linear-gradient(90deg,var(--gold) 0%,#dcbc5a 55%,rgba(243,231,192,.3) 100%)}
.cta-body{height:176px;background:var(--blue);border-radius:0 0 14px 14px;
  padding:24px 66px 0 31px;color:#fff;font-size:19px;line-height:24.5px;text-align:justify}

.contact{position:absolute;left:51px;top:1418px;width:1025px;height:60px}
.contact-label{position:absolute;left:0;top:0;width:264px;height:60px;background:var(--blue);
  border-radius:0 12px 12px 0;color:#fff;font-size:38px;line-height:62px;padding-left:55px;white-space:nowrap;
  box-shadow:4px 0 0 #fff}
.contact-bar{position:absolute;left:263px;top:0;width:762px;height:60px;background:var(--gold);overflow:hidden;
  display:flex;align-items:center;justify-content:space-between;padding:0 22px 0 24px;color:#fff;font-size:26px}
.contact-item{display:flex;align-items:center;gap:7px;line-height:1;white-space:nowrap;flex-shrink:0}
.contact-item svg{flex-shrink:0}
</style>
</head>
<body>
<main class="sheet">
  <header class="hero">
    <div class="hero-photo" role="img" aria-label="Faded blue-toned photo of a laptop and phone with document icons"></div>
    <div class="brand"><span class="brand-mark"></span><span class="brand-name">Keystone Records Inc</span></div>
    <h1 class="headline display">
      <span class="gold">Transform your</span> School’s<br>
      Document Management <span class="gold">with</span><br>
      <span class="gold">our comprehensive solutions</span>
    </h1>
  </header>

  <h2 class="intro-title display">Streamline, Secure, and <span class="gold">Simplify</span></h2>
  <p class="intro body-text">Managing school documents efficiently is crucial for smooth operations, compliance, and productivity. Our document processing services provide innovative solutions tailored for educational institutions, ensuring secure and seamless document and data handling.</p>

  <h3 class="band band-services display">Our Services</h3>

  <section class="service" style="left:46px">
    <svg class="service-icon" viewBox="0 0 74 74" fill="none" stroke-width="2.2">
      <rect x="22" y="4" width="36" height="44" stroke="var(--blue)"/>
      <rect x="14" y="12" width="36" height="44" fill="#fff" stroke="var(--blue)"/>
      <polyline points="20,34 28,26 34,30 44,20" stroke="var(--gold)"/>
      <circle cx="24" cy="48" r="10" fill="var(--gold)" stroke="none"/>
      <line x1="16" y1="56" x2="2" y2="70" stroke="var(--gold)" stroke-width="3"/>
      <path d="M20 45h8M20 49h8M20 53h6" stroke="#fff"/>
    </svg>
    <h4 class="service-title display" style="left:78px">Document Scan-<br>ning &amp; Conversion</h4>
    <ul class="service-list body-text" style="left:46px;width:240px">
      <li>Convert paper records into digital formats for easy access and storage.</li>
      <li>High-speed scanning for student records, administrative files, and historical archives.</li>
      <li>OCR (Optical Character Recognition) for searchable and editable documents.</li>
    </ul>
  </section>
  <div class="divider" style="left:351px"></div>

  <section class="service" style="left:415px">
    <svg class="service-icon" viewBox="0 0 74 74" fill="none" stroke-width="2.6">
      <path d="M16 44a12 12 0 0 1 2-24 18 18 0 0 1 34 0 12 12 0 0 1 6 22" stroke="var(--gold)"/>
      <path d="M37 42V24m-7 7 7-7 7 7" stroke="var(--gold)"/>
      <rect x="22" y="44" width="30" height="24" stroke="var(--blue)"/>
      <path d="M28 56h18M28 62h14" stroke="var(--gold)"/>
    </svg>
    <h4 class="service-title display" style="left:97px;top:13px">Cloud-Based Document<br>Management</h4>
    <ul class="service-list body-text" style="left:72px;width:240px">
      <li>Secure, centralized document storage accessible from anywhere.</li>
      <li>Role-based access controls for administrators, teachers, and staff.</li>
      <li>Automated backups and compliance with educational data security standards.</li>
    </ul>
  </section>
  <div class="divider" style="left:743px"></div>

  <section class="service" style="left:790px">
    <svg class="service-icon" viewBox="0 0 74 74" fill="none" stroke-width="2.4">
      <circle cx="50" cy="37" r="14" stroke="var(--gold)" stroke-width="9" stroke-dasharray="6 4"/>
      <circle cx="50" cy="37" r="6" fill="var(--gold)"/>
      <path d="M6 22h20l8 10M6 37h30M6 52h20l8-10" stroke="var(--blue)"/>
      <circle cx="6" cy="22" r="3" fill="var(--gold)"/><circle cx="6" cy="37" r="3" fill="var(--gold)"/><circle cx="6" cy="52" r="3" fill="var(--gold)"/>
    </svg>
    <h4 class="service-title display" style="left:96px;top:12px">Workflow<br>Automation</h4>
    <ul class="service-list body-text" style="left:55px;width:230px">
      <li>Digitize and streamline approval processes for enrollment, transcripts, and HR forms.</li>
      <li>Reduce paperwork and improve efficiency with automated workflows.</li>
      <li>Integration capable with existing school management systems.</li>
    </ul>
  </section>

  <h3 class="band band-why display">Why Choose Us?</h3>
  <ul class="reasons body-text">
    <li class="reason"><svg width="20" height="20" viewBox="0 0 20 20" fill="none" stroke-width="2"><circle cx="10" cy="10" r="8" stroke="var(--blue)"/><path d="M6 10l3 3 7-8" stroke="var(--gold)"/></svg>
      <div class="reason-title display">Increased Efficiency</div><div class="reason-text">Save time with digital workflows and instant document retrieval.</div></li>
    <li class="reason"><svg width="20" height="20" viewBox="0 0 20 20" fill="none" stroke-width="2"><circle cx="10" cy="10" r="8" stroke="var(--blue)"/><path d="M6 10l3 3 7-8" stroke="var(--gold)"/></svg>
      <div class="reason-title display">Enhanced Security</div><div class="reason-text">Protect sensitive student and faculty information.</div></li>
    <li class="reason"><svg width="20" height="20" viewBox="0 0 20 20" fill="none" stroke-width="2"><circle cx="10" cy="10" r="8" stroke="var(--blue)"/><path d="M6 10l3 3 7-8" stroke="var(--gold)"/></svg>
      <div class="reason-title display">Cost Savings</div><div class="reason-text">Reduce paper, printing, and storage costs.</div></li>
    <li class="reason"><svg width="20" height="20" viewBox="0 0 20 20" fill="none" stroke-width="2"><circle cx="10" cy="10" r="8" stroke="var(--blue)"/><path d="M6 10l3 3 7-8" stroke="var(--gold)"/></svg>
      <div class="reason-title display">Eco-Friendly</div><div class="reason-text">Minimize your school’s carbon footprint by going digital.</div></li>
  </ul>

  <aside class="cta">
    <h3 class="cta-head display">Get Started Today!</h3>
    <p class="cta-body body-text">Let us help you modernize your document processing system. Contact us for a free consultation and discover how our solutions can transform your school's document management.</p>
  </aside>

  <footer class="contact display">
    <div class="contact-label">Contact Us</div>
    <div class="contact-bar">
      <span class="contact-item"><svg width="20" height="20" viewBox="0 0 24 24" fill="var(--blue)"><path d="M6.6 10.8a15 15 0 0 0 6.6 6.6l2.2-2.2a1 1 0 0 1 1-.25 11.4 11.4 0 0 0 3.6.57 1 1 0 0 1 1 1V20a1 1 0 0 1-1 1A17 17 0 0 1 3 4a1 1 0 0 1 1-1h3.5a1 1 0 0 1 1 1c0 1.25.2 2.45.57 3.6a1 1 0 0 1-.25 1z"/></svg>555-014-2200</span>
      <span class="contact-item"><svg width="22" height="16" viewBox="0 0 22 16" fill="none" stroke="var(--blue)" stroke-width="2"><rect x="1" y="1" width="20" height="14"/><path d="M1 1l10 8 10-8"/></svg>info@keystonerecords.com</span>
      <span class="contact-item"><svg width="20" height="20" viewBox="0 0 20 20" fill="none" stroke="var(--blue)" stroke-width="1.6"><circle cx="10" cy="10" r="8.5"/><ellipse cx="10" cy="10" rx="3.8" ry="8.5"/><path d="M1.5 10h17M3 5.5h14M3 14.5h14"/></svg>www.keystonerecords.com</span>
    </div>
  </footer>
</main>
</body>
</html>
```